Marina Web Page

I'm looking for a visually engaging web page/layout that I can use as the basis for a website for my Marina. I need to include page content that can be stored and updated in an include file to allow someone to easily manage content without editing html or needing to understand html.

The business is a small marina and fishing center located on the Pamlico sound in eastern North Carolina right off the Intracoastal Waterway. We offer wet slips with power, water, and wifi and also have powered RV slips for camping available. The Marina sells fuel, beer, tackle/bait, and ice. The Marina also has an island style bar (The Gullwing Bar) and live music most weekends. The bar has a mascot named Dusty, short for captain, who is a black labradoodle know for diving to the bottom of the marina basin to retrieve oysters and rocks. Dusty could be incorporated as a minor design element but isn't a requirement.The marina caters to coastal sportsmen interested in sound fishing as well as offshore sport fishing. The Marina also offers fishing charters form a 32' Brinewood fishing boat w/ tuna tower.

The primary purpose of the initial version of the website is to communicate information about up coming events, music, bar specials etc... It will also be used to feature our services, fishing report and weather info, where we are located from both land and water, and a photo gallery.

Target Market(s)

Coastal sports enthusiast and the coastal boating community

Industry/Entity Type

Business

Requirements
Must have
• I would like animated menus incorporated into the page temple. It must also allow for the updating/storing of page content in a separate file to that an employee of the marina can update specials and events without having to understand or edit html.
Nice to have
• A photo gallery option that will present photos from a folder on the web server. Changing photos should be as easy as adding or deleting photos from the folder.

```html
<!DOCTYPE html>
<html lang="en">
<head>
<meta charset="utf-8">
<title>Heron Point Marina</title>
<link href="https://fonts.googleapis.com/css2?family=Bitter:wght@400;700&family=Oswald:wght@500&family=Arimo:wght@400;700&display=swap" rel="stylesheet">
<style>
:root{
  --blue:#1a5aa6;
  --blue-dark:#164c8e;
  --yellow:#fedb3c;
  --ink:#222;
  --muted:#8a8a8a;
  --row:#f0f0f0;
  --footer:#2b2b2b;
  --footer-base:#1b1b1b;
  --link:#1a5aa6;
}
*{margin:0;padding:0;box-sizing:border-box}
html,body{width:1168px;height:1200px;overflow:hidden}
body{position:relative;background:#fff;font-family:"Arimo",Arial,sans-serif;color:var(--ink)}
a{color:inherit;text-decoration:none}
.abs{position:absolute}

.topbar{left:0;top:0;width:1168px;height:17px;background:var(--blue);color:#fff;font-size:7.5px}
.topbar .account{left:296px;top:4px;text-decoration:underline}
.topbar .utility{left:782px;top:4px;display:flex;gap:5px;align-items:center}
.topbar svg{vertical-align:-1px}

.brand{left:295px;top:24px;display:flex;align-items:center;gap:6px;font-family:"Bitter",serif;font-weight:700;color:var(--blue);font-size:17px}
.brand .mark{width:14px;height:14px;border-radius:50%;background:var(--yellow)}
.social-top{left:806px;top:28px;display:flex;gap:4px}
.social-top span,.social-foot span{display:block;border-radius:50%;background:#777}
.social-top span{width:13px;height:13px}
.nav{left:572px;top:47px;display:flex;font-family:"Bitter",serif;font-size:11px}
.nav a{padding:2px 8px 3px;line-height:13px}
.nav a.active{background:var(--yellow);border-radius:2px;font-weight:700;color:#333;padding:2px 10px 3px}

.hero{left:0;top:90px;width:1168px;height:277px;background:linear-gradient(180deg,#8aa38a 0%,#5b7e7e 22%,#4e8192 45%,#6f98a6 75%,#5d8796 100%)}
.hero-arrow{top:216px;width:40px;height:40px;background:rgba(70,70,70,.75);display:flex;align-items:center;justify-content:center}
.hero-title{left:295px;top:270px;height:40px;padding:0 10px;background:#0e0e0e;color:#fff;font-family:"Oswald",sans-serif;font-size:29px;line-height:40px;width:242px}
.hero-caption{left:295px;top:318px;width:338px;height:39px;background:var(--yellow);font-size:10px;line-height:14px;padding:5px 10px;color:#333}
.hero-caption em{font-style:italic}

.section-title{font-family:"Bitter",serif;font-size:18px;color:#333;width:1168px;text-align:center}
.events-title{top:391px;display:flex;justify-content:center;align-items:center;gap:6px}
.event{top:436px;width:182px}
.event .photo{height:137px}
.event .date{margin-top:14px;font-size:7.5px;color:#555}
.event h3{margin-top:8px;font-size:10.5px;font-weight:400;color:#111}
.event p{margin-top:6px;font-size:8px;line-height:12px;color:var(--muted)}

.gallery{left:0;top:681px;width:1168px;height:160px;background:var(--yellow)}
.gallery .section-title{position:absolute;top:12px;left:0}
.gallery .pager{position:absolute;left:853px;top:30px;display:flex;gap:2px}
.thumb{position:absolute;top:46px;width:91px}
.thumb .photo{height:70px;border:2px solid #fff}
.thumb p{margin-top:9px;text-align:center;font-size:8px;color:#333}

.block-title{font-family:"Bitter",serif;font-size:16px;color:#222;display:flex;align-items:center;gap:6px}
.services{left:295px;top:866px;width:253px}
.service-list{list-style:none;margin-top:10px}
.service-list li{display:flex;align-items:center;height:24px;margin-bottom:1px;background:var(--row);font-size:10.5px;color:#333}
.service-list .num{width:28px;height:24px;background:var(--blue);color:#fff;font-size:12px;display:flex;align-items:center;justify-content:center}
.service-list .label{flex:1;padding-left:15px}
.service-list .go{width:9px;height:9px;border-radius:50%;background:#c8c8c8;margin-right:10px}
.more{display:block;text-align:right;font-size:7.5px;color:var(--link);text-decoration:underline;margin-top:6px}

.blog{left:585px;top:866px;width:288px}
.blog .intro{margin-top:7px;font-size:8px;line-height:12px;color:#666}
.post{display:flex;gap:14px;margin-top:10px;height:38px}
.post .photo{width:47px;height:38px;flex:none;border:1px solid #ccc}
.post h4{font-weight:400;font-size:8.5px;color:#111;margin-top:2px}
.post .sub{font-size:7.5px;color:#777;margin-top:3px}
.post .when{font-size:7.5px;color:var(--link);margin-top:3px}

.footer{left:0;top:1050px;width:1168px;height:125px;background:var(--footer);color:#fff;text-align:center}
.footer h2{font-family:"Bitter",serif;font-weight:400;font-size:16px;margin-top:23px}
.footer .contact{font-size:8.5px;color:#bbb;margin-top:10px}
.footer .links{font-size:8.5px;color:#ddd;margin-top:5px}
.social-foot{display:flex;justify-content:center;gap:6px;margin-top:10px}
.social-foot span{width:18px;height:18px;background:#8a8a8a}
.copyright{left:0;top:1175px;width:1168px;height:25px;background:var(--footer-base);color:#999;font-size:8px;padding:10px 0 0 295px}
.copyright b{font-weight:400;color:#ddd}
</style>
</head>
<body>

<header>
  <div class="topbar abs">
    <a class="account abs" href="#">Creat my account</a>
    <div class="utility abs">
      <svg width="7" height="7" viewBox="0 0 8 8"><circle cx="4" cy="2.3" r="2" fill="#fff"/><path d="M0 8c0-3 8-3 8 0z" fill="#fff"/></svg>
      <a href="#">Login</a><span>|</span>
      <svg width="7" height="7" viewBox="0 0 8 8"><text x="1.5" y="7" font-size="8" font-weight="700" fill="#fff" font-family="Arial">?</text></svg>
      <a href="#">Help Center</a>
    </div>
  </div>

  <a class="brand abs" href="#"><span class="mark"></span>Heron Point Marina</a>
  <div class="social-top abs"><span></span><span></span><span></span><span></span></div>
  <nav class="nav abs">
    <a class="active" href="#">Home</a><a href="#">Advanture</a><a href="#">About</a><a href="#">Prices</a><a href="#">Checkout</a><a href="#">Contact</a>
  </nav>
</header>

<section class="hero abs" role="img" aria-label="Harbour photo with a covered wooden boat and moored fishing vessels"></section>
<a class="hero-arrow abs" style="left:255px" href="#"><svg width="12" height="14"><path d="M11 1 1 7l10 6z" fill="#ddd"/></svg></a>
<a class="hero-arrow abs" style="left:874px" href="#"><svg width="12" height="14"><path d="M1 1l10 6-10 6z" fill="#ddd"/></svg></a>
<h1 class="hero-title abs">LOREM IPSUM DOLOR</h1>
<p class="hero-caption abs">Lorem ipsum dolor sit amet, consectetur adipiscing elit. Sed tempor, urna ut accumsan porta, nisi ante aliquet lectus...<em>Read More</em></p>

<section>
  <h2 class="section-title events-title abs">
    <svg width="15" height="15"><circle cx="7.5" cy="7.5" r="7.5" fill="var(--blue)"/><path d="M9 4 5.5 7.5 9 11" stroke="#fff" stroke-width="2" fill="none"/></svg>
    Our Upcomming Evants
    <svg width="15" height="15"><circle cx="7.5" cy="7.5" r="7.5" fill="var(--blue)"/><path d="M6 4l3.5 3.5L6 11" stroke="#fff" stroke-width="2" fill="none"/></svg>
  </h2>
  <article class="event abs" style="left:295px">
    <div class="photo" role="img" aria-label="Waterfront marina building with decks" style="background:linear-gradient(180deg,#7f9dbd,#6a7a80 55%,#4f5a60)"></div>
    <p class="date">August 1 , 2013</p><h3>Lorem ipsum dolor sit amet</h3>
    <p>Lorem ipsum dolor sit amet, consectetur adipi-scing elit. Sed tempor, urna ut accumsan</p>
  </article>
  <article class="event abs" style="left:493px">
    <div class="photo" role="img" aria-label="Sport fishing boat running at speed" style="background:linear-gradient(160deg,#4a5a63,#7d8c90 50%,#3e4b52)"></div>
    <p class="date">August 1 , 2013</p><h3>Lorem ipsum dolor sit amet</h3>
    <p>Lorem ipsum dolor sit amet, consectetur adipi-scing elit. Sed tempor, urna ut accumsan</p>
  </article>
  <article class="event abs" style="left:691px">
    <div class="photo" role="img" aria-label="Dog leaping off a dock into the marina basin" style="background:linear-gradient(180deg,#a7b2ad,#7e8a83 50%,#6d7b80)"></div>
    <p class="date">August 1 , 2013</p><h3>Lorem ipsum dolor sit amet</h3>
    <p>Lorem ipsum dolor sit amet, consectetur adipi-scing elit. Sed tempor, urna ut accumsan</p>
  </article>
</section>

<section class="gallery abs">
  <h2 class="section-title">Photo Gallery</h2>
  <div class="pager">
    <svg width="7" height="10"><path d="M6 1 2 5l4 4" stroke="#333" stroke-width="1.6" fill="none"/></svg>
    <svg width="7" height="10"><path d="M1 1l4 4-4 4" stroke="#333" stroke-width="1.6" fill="none"/></svg>
  </div>
  <div class="thumb" style="left:296px"><div class="photo" role="img" aria-label="Angler fishing by green water" style="background:linear-gradient(135deg,#6f9a2e,#a9c96a 55%,#8ab0c8)"></div><p>Lorem ipsum dolor</p></div>
  <div class="thumb" style="left:393px"><div class="photo" role="img" aria-label="Adult and child fishing together" style="background:linear-gradient(135deg,#4a5a3a,#8fa66b 50%,#7aa0b8)"></div><p>Lorem ipsum dolor</p></div>
  <div class="thumb" style="left:490px"><div class="photo" role="img" aria-label="Fishing reel over blue sea" style="background:linear-gradient(135deg,#2f8fc0,#7fc3d8 55%,#3a7ba0)"></div><p>Lorem ipsum dolor</p></div>
  <div class="thumb" style="left:587px"><div class="photo" role="img" aria-label="Angler fishing by green water" style="background:linear-gradient(135deg,#6f9a2e,#a9c96a 55%,#8ab0c8)"></div><p>Lorem ipsum dolor</p></div>
  <div class="thumb" style="left:684px"><div class="photo" role="img" aria-label="Adult and child fishing together" style="background:linear-gradient(135deg,#4a5a3a,#8fa66b 50%,#7aa0b8)"></div><p>Lorem ipsum dolor</p></div>
  <div class="thumb" style="left:781px"><div class="photo" role="img" aria-label="Fishing reel over blue sea" style="background:linear-gradient(135deg,#2f8fc0,#7fc3d8 55%,#3a7ba0)"></div><p>Lorem ipsum dolor</p></div>
</section>

<section class="services abs">
  <h2 class="block-title">
    <svg width="19" height="19" viewBox="0 0 20 20"><g fill="#333"><circle cx="10" cy="10" r="7"/><rect x="8.3" y="0.5" width="3.4" height="19" rx="1"/><rect x="8.3" y="0.5" width="3.4" height="19" rx="1" transform="rotate(45 10 10)"/><rect x="8.3" y="0.5" width="3.4" height="19" rx="1" transform="rotate(90 10 10)"/><rect x="8.3" y="0.5" width="3.4" height="19" rx="1" transform="rotate(135 10 10)"/></g><circle cx="10" cy="10" r="3" fill="#fff"/></svg>
    Our Services
  </h2>
  <ul class="service-list">
    <li><span class="num">1.</span><span class="label">Fishing Report</span><span class="go"></span></li>
    <li><span class="num">2.</span><span class="label">Music</span><span class="go"></span></li>
    <li><span class="num">3.</span><span class="label">Bar specials</span><span class="go"></span></li>
    <li><span class="num">4.</span><span class="label">Weather info</span><span class="go"></span></li>
  </ul>
  <a class="more" href="#">View more..</a>
</section>

<section class="blog abs">
  <h2 class="block-title">
    <svg width="15" height="13" viewBox="0 0 15 13"><g fill="#333"><rect x="0" y="0" width="3" height="3"/><rect x="4.5" y="0" width="10.5" height="3"/><rect x="0" y="5" width="3" height="3"/><rect x="4.5" y="5" width="10.5" height="3"/><rect x="0" y="10" width="3" height="3"/><rect x="4.5" y="10" width="10.5" height="3"/></g></svg>
    Recent blog post
  </h2>
  <p class="intro">Donec sed odio dui. Etiam porta sem malesuada magna mollis euismod. Nid dolor id nibh ultricies vehicula ut id elit. Morbi leo.</p>
  <div class="post">
    <div class="photo" role="img" aria-label="Harbour with boats" style="background:linear-gradient(180deg,#8a9a90,#4f8095)"></div>
    <div><h4>Vestibulum at eros. Praesent commodo cursus magna,</h4><p class="sub">Vestibulum at eros</p><p class="when">21 st january</p></div>
  </div>
  <div class="post">
    <div class="photo" role="img" aria-label="Angler fishing" style="background:linear-gradient(135deg,#6f9a2e,#a9c96a)"></div>
    <div><h4>Vestibulum at eros. Praesent commodo cursus magna,</h4><p class="sub">Vestibulum at eros</p><p class="when">21 st january</p></div>
  </div>
  <a class="more" href="#">View more..</a>
</section>

<footer class="footer abs">
  <h2>Get in Touch</h2>
  <p class="contact">Heron Point Marina.. Phone: (555) 010-4821 Fax: (555) 010-4822 Email: info@heronpointmarina.example</p>
  <p class="links">Home &nbsp;|&nbsp; Advanture &nbsp;|&nbsp; About &nbsp;|&nbsp; Prices &nbsp;|&nbsp; Checkout &nbsp;|&nbsp; Contact</p>
  <div class="social-foot"><span></span><span></span><span></span><span></span></div>
</footer>
<div class="copyright abs">Copyright © 2013 <b>heronpointmarina.example</b></div>

</body>
</html>
```